Reaching the Root: Reasoning in Clinical Choice-Making

I'd like a cover that looks like it would fit on the shelf next to "The Symptom Mirage" by Harold Vintner, "The Fall of Forgetting" by Carl Mortenson, "Meal Mend" by Neil Forsby, "The Energy Renewal Plan" by Owen Prichardson or "The Gland Renewal Plan" by the same or "The Cortex Renewal Plan" by the same ... either text only (with some interesting fonts that make the title stand out, and the subtitle smaller) or a relevant image, though I'm not entirely sure what that would be since this is a book about big-picture medical decision making.
Author name is Dr Miriam Oakhurst, NMD
I'll eventually request an e-book, paperback, and audio cover from the winner...

Target Market(s)

practicing physicians

Industry/Entity Type

medicine

Requirements
Must have
• look similar to other books in the genre

```html
<!DOCTYPE html>
<html lang="en">
<head>
<meta charset="utf-8">
<title>Reaching the Root — Book Cover</title>
<link href="https://fonts.googleapis.com/css2?family=Bebas+Neue&family=Arimo:wght@400&display=swap" rel="stylesheet">
<style>
  :root {
    --page: #ffffff;
    --cover: #0a0c0f;
    --red: #d40f0f;
    --white: #ffffff;
    --maze-light: #4a4d52;
    --maze-dark: #0a0c0f;
  }
  html, body {
    margin: 0;
    padding: 0;
    width: 1200px;
    height: 1200px;
    overflow: hidden;
    background: var(--page);
  }
  .book-cover {
    position: absolute;
    left: 200px;
    top: 0;
    width: 800px;
    height: 1200px;
    background: var(--cover);
  }
  .book-cover svg {
    display: block;
    width: 800px;
    height: 1200px;
  }
  .subtitle {
    font-family: "Arimo", Arial, sans-serif;
    font-size: 35px;
    fill: var(--white);
  }
  .title-display {
    font-family: "Bebas Neue", Impact, sans-serif;
  }
  .title-top { font-size: 286px; fill: var(--white); }
  .title-joiner { font-size: 63px; fill: var(--white); letter-spacing: 8px; }
  .title-bottom { font-size: 500px; fill: var(--red); }
  .rule { fill: var(--red); }
  .author {
    font-family: "Bebas Neue", Impact, sans-serif;
    font-size: 63px;
    fill: var(--white);
  }
</style>
</head>
<body>
  <div class="book-cover">
    <svg viewBox="0 0 800 1200" xmlns="http://www.w3.org/2000/svg">
      <defs>
        <radialGradient id="mazeGlow" cx="50%" cy="50%" r="50%">
          <stop offset="0%" stop-color="#8a2020"/>
          <stop offset="25%" stop-color="var(--maze-light)"/>
          <stop offset="100%" stop-color="var(--maze-dark)" stop-opacity="0"/>
        </radialGradient>
      </defs>

      <text class="subtitle" x="68" y="92" textLength="666" lengthAdjust="spacingAndGlyphs">REASONING IN CLINICAL CHOICE-MAKING</text>
      <rect class="rule" x="62" y="124" width="672" height="4"/>

      <text class="title-display title-top" x="62" y="352" textLength="672" lengthAdjust="spacingAndGlyphs">REACHING</text>

      <rect class="rule" x="62" y="388" width="262" height="4"/>
      <text class="title-display title-joiner" x="401" y="412" text-anchor="middle">THE</text>
      <rect class="rule" x="478" y="388" width="256" height="4"/>

      <text class="title-display title-bottom" x="62" y="782" textLength="672" lengthAdjust="spacingAndGlyphs">ROOT</text>

      <ellipse role="img" aria-label="Circular dark maze seen at an angle with a glowing red path rising from its centre as an upward arrow" cx="396" cy="944" rx="324" ry="96" fill="url(#mazeGlow)"/>

      <text class="author" x="84" y="1148" textLength="636" lengthAdjust="spacing">DR MIRIAM OAKHURST, NMD</text>
    </svg>
  </div>
</body>
</html>
```